Business card design for Velvet Harbor

We need business cards designed for our new marketing consulting company, Velvet Harbor. Our services include marketing strategy, go-to-market and launch planning, growth strategy, and execution. We serve medical technology and health technology companies, from startups to well-established growth companies.

The business cards should feel professional, credible, reliable and trustworthy, and should instill confidence. Also bold, creative, and modern.

The design must use the Velvet Harbor logo.

The primary brand color is this orange: #FF5501
A secondary color that you can use is this gray: #282B2D
I would prefer only to use the orange and gray. But if you feel you really need an additional accent color (please use it very sparingly, as little as possible), you can use this blue for small accent purposes: #009FED

Attached are the logo files. The main logo is the one with a little bit of orange on the left and the rest is gray.

The business card should include the following:

Velvet Harbor logo
First name and last name
Title
Email address
Phone number and type (in whatever order looks best for the design
Website (the website does not need to be in the same block as the personal info)

For example:

Nessa Pryle
Founder & Principal
nessa@velvetharbor.com
+1.628.309.4156 mobile (can use "." or spaces in between blocks of numbers)
velvetharbor.com (somewhere on the card, it does not need to be with the personal info; and note that there is no "www." at the beginning)

Note that there will be no address listed on the business card.

Target Market(s)

Executives (CEO, head of marketing, head of sales) at medical technology and health technology companies, mostly in their 40s and older, well-educated, often with advanced degrees. They are strategic thinkers, responsible for budgets, and familiar with P&L. Their comfort with and trust in using outside consultants varies.

Industry/Entity Type

Medical technology and health technology companies.

Contact Information for Business Card

See project description

Font styles to use
Sans Serif

Requirements
Must have
• Logo and see Business card details section above.

```html
<!DOCTYPE html>
<html lang="en">
<head>
<meta charset="utf-8">
<title>Velvet Harbor — Business Card</title>
<link rel="stylesheet" href="https://fonts.googleapis.com/css2?family=Montserrat:wght@400;500;700&display=swap">
<style>
  :root {
    --backdrop: #3a3a3a;
    --card: #1b1b1b;
    --card-deep: #111111;
    --pattern-mid: #262626;
    --pattern-light: #3d3d3d;
    --orange: #ff5501;
    --white: #ffffff;
    --muted: #d9d9d9;
  }
  * { margin: 0; padding: 0; box-sizing: border-box; }
  html, body {
    width: 1200px; height: 801px; overflow: hidden;
    background: var(--backdrop);
    font-family: "Montserrat", sans-serif;
  }
  .stage {
    position: relative; width: 1200px; height: 801px;
    display: flex; align-items: center; justify-content: center; gap: 48px;
  }
  .card {
    position: relative; width: 520px; height: 297px;
    background: var(--card);
    border-bottom: 2px solid var(--orange);
    border-right: 2px solid var(--orange);
    overflow: hidden;
  }
  /* Brand lockup: plain square beside the name */
  .brand {
    display: flex; align-items: center; gap: 20px;
  }
  .brand-square {
    width: 22px; height: 22px; flex: none;
    background: var(--orange);
  }
  .brand-name {
    color: var(--white); font-weight: 500;
    font-size: 30px; line-height: 1.05; letter-spacing: 0.22em;
    text-transform: uppercase;
  }
  /* Front */
  .card-front .brand { position: absolute; left: 48px; top: 60px; }
  .details {
    position: absolute; left: 48px; right: 40px; bottom: 50px;
    display: flex; align-items: center;
  }
  .person { width: 190px; }
  .person-name {
    color: var(--orange); font-weight: 700; font-size: 20px;
    letter-spacing: 0.03em; text-transform: uppercase;
  }
  .person-title { color: var(--white); font-size: 14px; margin-top: 4px; }
  .divider { width: 1px; height: 66px; background: var(--orange); margin: 0 22px 0 0; }
  .contacts { list-style: none; display: flex; flex-direction: column; gap: 7px; }
  .contacts li {
    display: flex; align-items: center; gap: 9px;
    color: var(--muted); font-size: 13px;
  }
  .contacts svg { width: 12px; height: 12px; flex: none; }
  /* Back */
  .pattern {
    position: absolute; inset: 0;
    background: linear-gradient(115deg, var(--card-deep) 0%, var(--pattern-mid) 50%, var(--pattern-light) 100%);
  }
  .card-back .brand {
    position: absolute; left: 50%; top: 50%;
    transform: translate(-50%, -50%);
  }
</style>
</head>
<body>
<main class="stage">
  <section class="card card-front" aria-label="Business card front">
    <div class="brand">
      <span class="brand-square" aria-hidden="true"></span>
      <p class="brand-name">Velvet<br>Harbor</p>
    </div>
    <div class="details">
      <div class="person">
        <p class="person-name">Nessa Pryle</p>
        <p class="person-title">Founder &amp; Principal</p>
      </div>
      <span class="divider"></span>
      <ul class="contacts">
        <li>
          <svg viewBox="0 0 12 12" aria-hidden="true"><path d="M2.5 1h2l1 3-1.3 1a6 6 0 0 0 2.8 2.8l1-1.3 3 1v2a1 1 0 0 1-1 1A9.5 9.5 0 0 1 1.5 2a1 1 0 0 1 1-1z" fill="var(--orange)"/></svg>
          +1.628.309.4156
        </li>
        <li>
          <svg viewBox="0 0 12 12" aria-hidden="true"><rect x="0.5" y="2" width="11" height="8" rx="1" fill="var(--orange)"/><path d="M1 2.8 6 6.5l5-3.7" fill="none" stroke="var(--card)" stroke-width="1"/></svg>
          nessa@velvetharbor.com
        </li>
        <li>
          <svg viewBox="0 0 12 12" aria-hidden="true"><circle cx="6" cy="6" r="5" fill="none" stroke="var(--orange)" stroke-width="1.4"/><path d="M1 6h10M6 1c-2.5 3-2.5 7 0 10M6 1c2.5 3 2.5 7 0 10" fill="none" stroke="var(--orange)" stroke-width="1"/></svg>
          velvetharbor.com
        </li>
      </ul>
    </div>
  </section>

  <section class="card card-back" aria-label="Business card back">
    <div class="pattern" role="img" aria-label="Embossed repeating pattern of the brand symbol across the card, fading from black at left to grey at right"></div>
    <div class="brand">
      <span class="brand-square" aria-hidden="true"></span>
      <p class="brand-name">Velvet<br>Harbor</p>
    </div>
  </section>
</main>
</body>
</html>
```